Tarn - Stationary Design/Layout

We are a well established clothing design and manufacturing company (Tarn Sourcing) based in London UK, with our own factory in Bangladesh, supplying to many fashion retailers and brands. Our factory has very high environmental and ethical standards with people at its heart. Our quality of garments are second to none.
Our new logo has been proudly developed by the Pixel Guild community last month, we are now in the second phase and need the layout designed for our letterheads, double sided business cards, compliment slip and clothing ticket. Feel as creative as you like, but make sure it looks great!!
***The Logo - the logo design and colour is set and should NOT be changed and stay on a dark grey backround. The logo artwork to use is attached.
***Details to use for the business card:
Dorian Pelham
Direct Line: 020 7946 0158
dorian@tarnsourcing-example.com
Tarn Sourching Ltd.
57 - 59 Hollin Row
Calder . Wrenfold
NW9 4QT
Switchboard: 020 7946 0274
Fax: 020 7946 0274
www.tarnsourcing-example.co.uk
***Details to use for the letterhead and compliment slip:
Tarn Sourching Ltd.
57 - 59 Hollin Row
Calder . Wrenfold
NW9 4QT
Fax: 020 7946 0274
www.tarnsourcing-example.co.uk
***Details for Swing Ticket:
Size: 12cm height by 5.5cm width
One side need to have just the logo without the 'Sourcing', on the other it needs to stay blank

```html
<!DOCTYPE html>
<html lang="en">
<head>
<meta charset="utf-8">
<title>Tarn Sourcing – Business Card</title>
<link href="https://fonts.googleapis.com/css2?family=Poppins:wght@300;500;600&display=swap" rel="stylesheet">
<style>
  :root {
    --board: #d1d4d5;
    --card: #3d3d3d;
    --teal: #a6dde3;
    --white: #ffffff;
    --soft: #d2d2d2;
    --rule: #8a8a8a;
  }
  * { margin: 0; padding: 0; box-sizing: border-box; }
  html, body { width: 960px; height: 1200px; overflow: hidden; }
  body {
    background: var(--board);
    font-family: "Poppins", sans-serif;
    position: relative;
  }
  .card {
    position: absolute;
    left: 132px;
    width: 697px;
    height: 400px;
    background: var(--card);
    box-shadow: 3px 4px 6px rgba(0,0,0,0.35);
  }
  .card--front { top: 140px; }
  .card--back { top: 659px; }

  .contact {
    position: absolute;
    left: 48px;
    top: 48px;
    color: var(--soft);
    font-weight: 300;
    font-size: 17px;
    line-height: 28px;
    white-space: nowrap;
  }
  .contact__name {
    color: var(--teal);
    font-weight: 500;
    font-size: 18px;
    text-transform: uppercase;
    margin-bottom: 14px;
  }
  .contact__label { color: var(--white); font-weight: 600; }
  .contact__company {
    color: var(--teal);
    font-weight: 500;
    margin-top: 14px;
  }

  .divider {
    position: absolute;
    left: 397px;
    top: 50px;
  }

  .brand-name {
    color: var(--teal);
    font-weight: 600;
    text-transform: uppercase;
    white-space: nowrap;
  }
  .brand-name--corner {
    position: absolute;
    right: 47px;
    top: 50px;
    font-size: 24px;
    letter-spacing: 1px;
  }
  .brand-name--centre {
    position: absolute;
    left: 0;
    right: 0;
    top: 160px;
    text-align: center;
    font-size: 54px;
    letter-spacing: 3px;
  }
</style>
</head>
<body>
  <section class="card card--front">
    <div class="contact">
      <p class="contact__name">Dorian Pelham</p>
      <p><span class="contact__label">direct line:</span> (020) 7946 0158</p>
      <p><span class="contact__label">switchboard:</span> (020) 7946 0274</p>
      <p><span class="contact__label">f:</span> (020) 7946 0274</p>
      <p><span class="contact__label">e:</span> dorian@tarnsourcing-example.com</p>
      <p><span class="contact__label">w:</span> www.tarnsourcing-example.co.uk</p>
      <p class="contact__company">Tarn Sourching Ltd.</p>
      <p>57 - 59 Hollin Row</p>
      <p>Calder . Wrenfold</p>
      <p>NW9 4QT</p>
    </div>

    <svg class="divider" width="4" height="300" viewBox="0 0 4 300" aria-hidden="true">
      <line x1="2" y1="0" x2="2" y2="300" stroke="var(--rule)" stroke-width="1.5" stroke-dasharray="19 20"/>
    </svg>

    <p class="brand-name brand-name--corner">Tarn Sourcing</p>
  </section>

  <section class="card card--back">
    <p class="brand-name brand-name--centre">Tarn Sourcing</p>
  </section>
</body>
</html>
```